Zielgruppe
Über die KALV:
Die KALV ist eine med. Vereinigung in der sich Ärzte aus allen Fachrichtungen zum Thema Adipositas austauschen.
Als 'Kestrel Alliance for Lipid and Vital Health Research Network' sind wir seit 1996 ein Pionier in der Schweiz im Bereich der krankhaften Adipositas und Stoffwechselstörungen.
Unsere Mitglieder - ein Zusammenschluss von Fachleuten, die sich mit Adipositas befassen - arbeiten eng zusammen, um das Verständnis und die Behandlung dieser Krankheit zu verbessern.
Aufgabenstellung
Die Farben der Präsentation sollten sich an den Farben unseres neuen Logos halten. Bitte verwenden Sie bei der Erstellung der Folienlayouts eine Schrift die allgemein bereits in den Microsoft Programmen enthalten sind. Es soll ein modernes und minimallistisches Design sein. Es geht bei diesem Auftrag um ein Grundlayout von Präsentationsfolien welches unsere Mitglieder verwenden wenn diese Vorträge halten.

```html
<!DOCTYPE html>
<html lang="de">
<head>
<meta charset="utf-8">
<title>KALV Präsentationsvorlage</title>
<link rel="stylesheet" href="https://fonts.googleapis.com/css2?family=Montserrat:wght@600;700;800&family=Arimo:wght@400;700&display=swap">
<style>
:root{
  --blue:#3f6db5;
  --blue-dark:#2f5aa0;
  --red:#c4121f;
  --board:#d0d0d0;
  --panel:#e6e6e6;
  --text:#8a8a8a;
  --white:#ffffff;
  --beige:#e8d9b8;
}
*{margin:0;padding:0;box-sizing:border-box}
html,body{width:1200px;height:683px;overflow:hidden}
body{background:var(--board);font-family:Arimo,Arial,sans-serif;position:relative;color:var(--text)}
.slide{position:absolute;width:339px;height:201px;background:var(--white);overflow:hidden}
.abs{position:absolute}
.title{position:absolute;left:19px;top:13px;font-family:Montserrat,Arial,sans-serif;font-weight:700;font-size:15px;letter-spacing:1.2px;color:var(--blue);line-height:1}
.subtitle{position:absolute;left:19px;top:29px;font-size:7px;color:var(--text);letter-spacing:.2px}
.bar-bottom{position:absolute;left:0;bottom:0;width:100%;height:5px;background:var(--red)}
.brand{position:absolute;display:flex;align-items:center;gap:2px;font-family:Montserrat,Arial,sans-serif;font-weight:800;font-size:9.5px;color:var(--blue);line-height:1}
.brand-mark{width:6px;height:6px;background:var(--red);display:inline-block}
.brand.foot{right:18px;bottom:9px}
.body-copy{font-size:5.8px;line-height:7.2px;color:var(--text)}
.item-head{font-family:Montserrat,Arial,sans-serif;font-weight:700;font-size:6px;color:var(--blue);letter-spacing:.2px}
.item-text{font-size:4.3px;line-height:5.3px;color:var(--text)}
.center{text-align:center}
svg{display:block}
.photo{position:absolute}
/* slide 1 */
.cover-band{position:absolute;left:149px;top:111px;width:190px;height:45px;background:rgba(63,109,181,.82)}
.cover-head{position:absolute;left:175px;top:116px;font-family:Montserrat,Arial,sans-serif;font-weight:800;font-size:21px;letter-spacing:2.5px;color:var(--white)}
.cover-sub{position:absolute;left:173px;top:141px;font-size:7.3px;color:var(--white)}
.cover-rule{position:absolute;left:0;top:163px;width:100%;height:1.5px;background:var(--red)}
.cover-brand{left:16px;top:170px;font-size:13px;gap:3px}
.cover-brand .brand-mark{width:8px;height:8px}
.cover-name{position:absolute;left:16px;top:182px;width:110px;font-size:5.2px;line-height:6.6px;color:var(--blue)}
/* slide 3 */
.contact-band{position:absolute;left:157px;top:0;width:38px;height:201px;background:var(--blue)}
.contact-icon{position:absolute;left:180px;width:22px;height:24px;background:var(--white);display:flex;align-items:center;justify-content:center}
.contact-sep{position:absolute;left:164px;width:25px;height:.8px;background:var(--white)}
/* slide 6 */
.table-head,.table-foot{position:absolute;left:31px;width:275px;height:17px;background:var(--blue);color:var(--white);font-size:4.6px}
.table-body{position:absolute;left:31px;top:66px;width:275px;height:88px;background:#f4f5f7}
.cell{position:absolute;transform:translateX(-50%);white-space:nowrap}
/* slide 7 */
.tile{position:absolute;top:62px;width:67px;height:39px;background:var(--panel);display:flex;align-items:center;justify-content:center}
/* slide 9 */
.col{position:absolute;top:2px;width:67px;height:195px;background:var(--panel)}
.col.active{background:var(--red)}
.col-num{position:absolute;top:19px;width:100%;text-align:center;font-family:Montserrat,Arial,sans-serif;font-weight:800;font-size:10px;color:var(--red)}
.col-head{position:absolute;top:92px;width:100%;text-align:center;font-family:Montserrat,Arial,sans-serif;font-weight:700;font-size:9px;letter-spacing:.8px;color:var(--blue)}
.col-line{position:absolute;width:100%;text-align:center;font-size:5.6px;letter-spacing:.5px;color:var(--text)}
.col-tag{position:absolute;top:158px;left:50%;transform:translateX(-50%);background:var(--red);color:var(--white);font-size:4.3px;padding:4px 3px;white-space:nowrap}
.col.active .col-num{color:var(--white);font-size:12px;top:16px}
.col.active .col-head,.col.active .col-line{color:var(--white)}
.col.active .col-tag{background:var(--white);color:var(--red);font-size:5.6px;padding:5px 2px}
</style>
</head>
<body>

<svg width="0" height="0" style="position:absolute" aria-hidden="true">
  <defs>
    <symbol id="ico-clipboard" viewBox="0 0 24 24"><g fill="none" stroke="currentColor" stroke-width="1.6"><rect x="5" y="4" width="14" height="17" rx="1.5"/><rect x="9" y="2.5" width="6" height="3" rx=".8"/><path d="M8 9h1M11 9h5M8 12.5h1M11 12.5h5M8 16h1M11 16h5"/></g></symbol>
    <symbol id="ico-steth" viewBox="0 0 24 24"><g fill="none" stroke="currentColor" stroke-width="1.6"><path d="M6 3v6a4 4 0 0 0 8 0V3"/><path d="M10 13v3a4 4 0 0 0 8 0v-2"/><circle cx="18" cy="11.5" r="2.3"/></g></symbol>
    <symbol id="ico-gauge" viewBox="0 0 24 24"><g fill="none" stroke="currentColor" stroke-width="1.5"><circle cx="8" cy="9" r="5"/><path d="M8 9l2-2"/><path d="M12 12c2 3 4 6 7 6"/><circle cx="19.5" cy="18.5" r="1.8" fill="currentColor"/></g></symbol>
    <symbol id="ico-kit" viewBox="0 0 24 24"><rect x="3" y="7" width="18" height="13" rx="1.5" fill="currentColor"/><path d="M9 7V5h6v2" fill="none" stroke="currentColor" stroke-width="1.6"/><path d="M12 10v7M8.5 13.5h7" stroke="#fff" stroke-width="2.4"/></symbol>
    <symbol id="ico-chart" viewBox="0 0 24 24"><g fill="currentColor"><rect x="5" y="12" width="3.5" height="7"/><rect x="10.2" y="8" width="3.5" height="11"/><rect x="15.4" y="5" width="3.5" height="14"/></g></symbol>
    <symbol id="pin" viewBox="0 0 36 46"><circle cx="18" cy="17" r="17" fill="currentColor"/><path d="M7 29L18 42L29 29Z" fill="#c9c9c9"/><circle cx="18" cy="17" r="17" fill="currentColor"/></symbol>
  </defs>
</svg>

<!-- Slide 1: cover -->
<section class="slide" style="left:66px;top:27px">
  <div class="photo" role="img" aria-label="Foto: Radfahrerpaar auf Mountainbikes vor blauem Himmel" style="left:0;top:0;width:339px;height:163px;background:linear-gradient(100deg,#5d9bd8 0%,#8fb8e0 35%,#c9c3c0 55%,#d9683a 80%,#b9532e 100%)"></div>
  <div class="cover-band"></div>
  <div class="cover-head">HEADLINE</div>
  <div class="cover-sub">Lorem ipsum dolor sit amet, consectetuer</div>
  <div class="cover-rule"></div>
  <div class="brand cover-brand"><i class="brand-mark"></i>KALV</div>
  <div class="cover-name">Kestrel Alliance for Lipid and Vital Health Research Network</div>
</section>

<!-- Slide 2: text -->
<section class="slide" style="left:431px;top:27px">
  <h2 class="title">LOREM IPSUM</h2>
  <p class="subtitle">Lorem ipsum dolor sit amet, consectetuer</p>
  <p class="abs body-copy" style="left:19px;top:67px;width:303px">Lorem ipsum dolor sit amet, consectetuer adipiscing elit, sed diam nonummy nibh euismod tincidunt ut laoreet dolore magna aliquam erat volutpat. Ut wisi enim ad minim veniam, quis nostrud exerci tation ullamcorper suscipit lobortis nisl ut aliquip ex ea commodo consequat. Duis autem vel eum iriure dolor in hendrerit in vulputate velit esse molestie consequat, vel illum dolore eu feugiat nulla facilisis at vero eros et accumsan et iusto odio dignissim qui blandit praesent luptatum zzril delenit augue duis dolore te feugait nulla facilisi.<br>Lorem ipsum dolor sit amet, cons ectetuer adipiscing elit, sed diam nonummy nibh euismod tincidunt ut laoreet dolore magna aliquam erat volutpat. Ut wisi enim ad minim veniam, quis nostrud exerci tation ullamcorper suscipit lobortis nisl ut aliquip ex ea commodo consequat.<br>Lorem ipsum dolor sit amet, consectetuer adipiscing elit, sed diam nonummy nibh euismod tincidunt ut laoreet dolore magna aliquam erat volutpat. Ut wisi enim ad minim veniam, quis nostrud exerci tation</p>
  <div class="brand foot"><i class="brand-mark"></i>KALV</div>
  <div class="bar-bottom"></div>
</section>

<!-- Slide 3: contact -->
<section class="slide" style="left:795px;top:27px">
  <div class="photo" role="img" aria-label="Foto: lächelnde Ärztin im weissen Kittel in heller Praxis" style="left:0;top:0;width:157px;height:201px;background:linear-gradient(90deg,#dfe6ea 0%,#e9d6c4 40%,#c99a6a 65%,#eef1f3 100%)"></div>
  <div class="brand" style="left:107px;top:186px"><i class="brand-mark"></i>KALV</div>
  <div class="contact-band"></div>
  <div class="contact-sep" style="top:49px"></div>
  <div class="contact-sep" style="top:99px"></div>
  <div class="contact-sep" style="top:150px"></div>
  <div class="contact-icon" style="top:13px"><svg width="14" height="11" viewBox="0 0 14 11"><rect x=".5" y=".5" width="13" height="10" fill="none" stroke="#c4121f"/><path d="M.5 .5L7 6l6.5-5.5M.5 10.5L5 5.5M13.5 10.5L9 5.5" fill="none" stroke="#c4121f"/></svg></div>
  <div class="contact-icon" style="top:63px"><svg width="11" height="14" viewBox="0 0 11 14"><path d="M5.5 13.5C2 9 1 7 1 5a4.5 4.5 0 0 1 9 0c0 2-1 4-4.5 8.5z" fill="#c4121f"/><circle cx="5.5" cy="5" r="2" fill="#fff"/></svg></div>
  <div class="contact-icon" style="top:114px"><svg width="14" height="14" viewBox="0 0 14 14"><circle cx="7" cy="7" r="6.5" fill="#c4121f"/><path d="M.5 7h13M7 .5v13M2.5 2.5c3 3 6 3 9 0M2.5 11.5c3-3 6-3 9 0" fill="none" stroke="#fff" stroke-width=".9"/></svg></div>
  <div class="contact-icon" style="top:164px"><svg width="13" height="12" viewBox="0 0 13 12"><path d="M6.5 0L0 6h2v6h3.5V8h2v4H11V6h2z" fill="#c4121f"/></svg></div>
  <div class="abs" style="left:224px;top:20px;width:100px"><div class="item-head" style="font-size:6.8px">LOREM IPSUM</div><p class="item-text" style="margin-top:1px">Lorem ipsum dolor sit amet, consectetuer adipiscing elit, sed diam nonummy nibh</p></div>
  <div class="abs" style="left:224px;top:70px;width:100px"><div class="item-head" style="font-size:6.8px">LOREM IPSUM</div><p class="item-text" style="margin-top:1px">Lorem ipsum dolor sit amet, consectetuer adipiscing elit, sed diam nonummy nibh</p></div>
  <div class="abs" style="left:224px;top:120px;width:100px"><div class="item-head" style="font-size:6.8px">LOREM IPSUM</div><p class="item-text" style="margin-top:1px">Lorem ipsum dolor sit amet, consectetuer adipiscing elit, sed diam nonummy nibh</p></div>
  <div class="abs" style="left:224px;top:171px;width:100px"><div class="item-head" style="font-size:6.8px">LOREM IPSUM</div><p class="item-text" style="margin-top:1px">Lorem ipsum dolor sit amet, consectetuer adipiscing elit, sed diam nonummy nibh</p></div>
</section>

<!-- Slide 4: process -->
<section class="slide" style="left:66px;top:241px">
  <h2 class="title">LOREM IPSUM</h2>
  <p class="subtitle">Lorem ipsum dolor sit amet, consectetuer</p>
  <svg class="abs" style="left:0;top:0" width="339" height="201">
    <line x1="60" y1="117" x2="278" y2="117" stroke="#c9c9c9" stroke-width=".8"/>
    <g fill="#3f6db5" font-family="Montserrat,Arial,sans-serif" font-weight="700" font-size="10" text-anchor="middle">
      <text x="60" y="70">1</text><text x="133" y="70">2</text><text x="206" y="70">3</text><text x="278" y="70">4</text>
    </g>
    <g color="#3f6db5">
      <use href="#pin" x="44" y="73" width="32" height="41"/>
      <use href="#pin" x="117" y="73" width="32" height="41"/>
      <use href="#pin" x="190" y="73" width="32" height="41"/>
      <use href="#pin" x="262" y="73" width="32" height="41"/>
    </g>
    <g color="#fff">
      <use href="#ico-clipboard" x="51" y="80" width="18" height="18"/>
      <use href="#ico-steth" x="124" y="80" width="18" height="18"/>
      <use href="#ico-gauge" x="197" y="80" width="18" height="18"/>
      <use href="#ico-kit" x="269" y="80" width="18" height="18"/>
    </g>
    <g fill="#c4121f"><circle cx="60" cy="117" r="1.8"/><circle cx="133" cy="117" r="1.8"/><circle cx="206" cy="117" r="1.8"/><circle cx="278" cy="117" r="1.8"/></g>
  </svg>
  <div class="abs center" style="left:35px;top:126px;width:50px"><div class="item-head">LOREM IPSUM</div><p class="item-text">Lorem ipsum dolor sit amet, consectetuer adipiscing elit, sed diam nonummy nibh</p></div>
  <div class="abs center" style="left:108px;top:126px;width:50px"><div class="item-head">LOREM IPSUM</div><p class="item-text">Lorem ipsum dolor sit amet, consectetuer adipiscing elit, sed diam nonummy nibh</p></div>
  <div class="abs center" style="left:181px;top:126px;width:50px"><div class="item-head">LOREM IPSUM</div><p class="item-text">Lorem ipsum dolor sit amet, consectetuer adipiscing elit, sed diam nonummy nibh</p></div>
  <div class="abs center" style="left:253px;top:126px;width:50px"><div class="item-head">LOREM IPSUM</div><p class="item-text">Lorem ipsum dolor sit amet, consectetuer adipiscing elit, sed diam nonummy nibh</p></div>
  <div class="brand foot"><i class="brand-mark"></i>KALV</div>
  <div class="bar-bottom"></div>
</section>

<!-- Slide 5: chart -->
<section class="slide" style="left:431px;top:241px">
  <h2 class="title">LOREM IPSUM</h2>
  <p class="subtitle">Lorem ipsum dolor sit amet, consectetuer</p>
  <svg class="abs" style="left:0;top:0" width="175" height="201">
    <g stroke="#d4d4d4" stroke-width=".5">
      <line x1="34" y1="84" x2="155" y2="84"/><line x1="34" y1="90" x2="155" y2="90"/><line x1="34" y1="96" x2="155" y2="96"/><line x1="34" y1="102" x2="155" y2="102"/><line x1="34" y1="108" x2="155" y2="108"/><line x1="34" y1="114" x2="155" y2="114"/><line x1="34" y1="121" x2="155" y2="121"/><line x1="34" y1="127" x2="155" y2="127"/><line x1="34" y1="133" x2="155" y2="133"/><line x1="34" y1="139" x2="155" y2="139"/><line x1="34" y1="145" x2="155" y2="145"/>
    </g>
    <g fill="#8a8a8a" font-size="3.6" font-family="Arimo,Arial,sans-serif" text-anchor="middle">
      <text x="20" y="86">100</text><text x="20" y="92">90</text><text x="20" y="98">80</text><text x="20" y="104">70</text><text x="20" y="110">60</text><text x="20" y="116">50</text><text x="20" y="123">40</text><text x="20" y="129">30</text><text x="20" y="135">20</text><text x="20" y="141">10</text><text x="20" y="147">0</text>
    </g>
    <g fill="#3f6db5" font-size="5.5" font-family="Arimo,Arial,sans-serif" text-anchor="middle">
      <text x="34" y="156">1</text><text x="64" y="156">2</text><text x="94" y="156">3</text><text x="124" y="156">4</text><text x="155" y="156">5</text>
    </g>
    <polyline points="34,120 64,126 94,112 124,113 155,92" fill="none" stroke="#555" stroke-width=".6"/>
    <g fill="#c4121f"><circle cx="34" cy="120" r="1.6"/><circle cx="64" cy="126" r="1.6"/><circle cx="94" cy="112" r="1.6"/><circle cx="124" cy="113" r="1.6"/><circle cx="155" cy="92" r="1.6"/></g>
    <g color="#3f6db5">
      <use href="#pin" x="28" y="99" width="12" height="16"/>
      <use href="#pin" x="58" y="105" width="12" height="16"/>
      <use href="#pin" x="88" y="91" width="12" height="16"/>
      <use href="#pin" x="118" y="92" width="12" height="16"/>
      <use href="#pin" x="149" y="71" width="12" height="16"/>
    </g>
    <g color="#fff">
      <use href="#ico-clipboard" x="31" y="102" width="6" height="6"/>
      <use href="#ico-steth" x="61" y="108" width="6" height="6"/>
      <use href="#ico-gauge" x="91" y="94" width="6" height="6"/>
      <use href="#ico-kit" x="121" y="95" width="6" height="6"/>
      <use href="#ico-chart" x="152" y="74" width="6" height="6"/>
    </g>
  </svg>
  <p class="abs body-copy" style="left:178px;top:73px;width:145px;text-align:justify">Lorem ipsum dolor sit amet, consectetuer adipiscing elit, sed diam nonummy nibh euismod tincidunt ut laoreet dolore magna aliquam erat volutpat. Ut wisi enim ad minim veniam, quis nostrud exerci tation ullamcorper suscipit lobortis nisl ut aliquip ex ea commodo consequat. Duis autem vel eum iriure dolor in hendrerit in vulputate velit esse molestie consequat, vel illum dolore eu feugiat nulla facilisis at vero eros et accumsan et iusto odio dignissim qui blandit praesent luptatum zzril delenit augue duis dolore te feugait nulla facilisi.</p>
  <div class="brand foot"><i class="brand-mark"></i>KALV</div>
  <div class="bar-bottom"></div>
</section>

<!-- Slide 6: table -->
<section class="slide" style="left:795px;top:241px">
  <h2 class="title">LOREM IPSUM</h2>
  <p class="subtitle">Lorem ipsum dolor sit amet, consectetuer</p>
  <div class="table-head" style="top:49px">
    <span class="cell" style="left:33px;top:6px">dolor sit amet</span><span class="cell" style="left:96px;top:6px">dolor sit amet</span><span class="cell" style="left:145px;top:6px">dolor sit amet</span><span class="cell" style="left:195px;top:6px">dolor sit amet</span><span class="cell" style="left:244px;top:6px">dolor sit amet</span>
  </div>
  <div class="table-body">
    <span class="cell" style="left:34px;top:9px;font-size:4px">Lorem ipsum dolor sit amet,</span>
    <span class="cell" style="left:34px;top:25px;font-size:4px">Lorem ipsum dolor sit amet,</span>
    <span class="cell" style="left:34px;top:41px;font-size:4px">Lorem ipsum dolor sit amet,</span>
    <span class="cell" style="left:34px;top:58px;font-size:4px">Lorem ipsum dolor sit amet,</span>
    <span class="cell" style="left:34px;top:74px;font-size:4px">Lorem ipsum dolor sit amet,</span>
  </div>
  <svg class="abs" style="left:0;top:0" width="339" height="201">
    <g fill="#3f6db5">
      <circle cx="127" cy="77" r="5"/><circle cx="127" cy="94" r="5"/>
      <circle cx="176" cy="77" r="5"/><circle cx="176" cy="94" r="5"/><circle cx="176" cy="110" r="5"/>
      <circle cx="226" cy="77" r="5"/><circle cx="226" cy="94" r="5"/><circle cx="226" cy="110" r="5"/><circle cx="226" cy="126" r="5"/>
    </g>
    <g fill="#c4121f"><circle cx="275" cy="77" r="5"/><circle cx="275" cy="94" r="5"/><circle cx="275" cy="110" r="5"/><circle cx="275" cy="126" r="5"/><circle cx="275" cy="143" r="5"/></g>
  </svg>
  <div class="table-foot" style="top:154px">
    <span class="cell" style="left:33px;top:6px">dolor sit amet</span><span class="cell" style="left:103px;top:6px">it amet</span><span class="cell" style="left:145px;top:6px">dolor sit amet</span><span class="cell" style="left:195px;top:6px">dolor sit amet</span><span class="cell" style="left:244px;top:6px">dolor sit amet</span>
  </div>
  <div class="brand foot"><i class="brand-mark"></i>KALV</div>
  <div class="bar-bottom"></div>
</section>

<!-- Slide 7: blue tiles -->
<section class="slide" style="left:66px;top:455px;background:var(--blue)">
  <h2 class="title" style="left:25px;color:var(--white)">LOREM IPSUM</h2>
  <p class="subtitle" style="left:25px;color:var(--beige)">Lorem ipsum dolor sit amet, consectetuer</p>
  <div class="tile" style="left:34px;color:var(--red)"><svg width="18" height="18"><use href="#ico-clipboard"/></svg></div>
  <div class="tile" style="left:102px;color:var(--red)"><svg width="18" height="18"><use href="#ico-steth"/></svg></div>
  <div class="tile" style="left:171px;color:var(--red)"><svg width="18" height="18"><use href="#ico-gauge"/></svg></div>
  <div class="tile" style="left:239px;color:var(--red)"><svg width="18" height="18"><use href="#ico-kit"/></svg></div>
  <svg class="abs" style="left:0;top:104px" width="339" height="8">
    <g fill="#d8d8d8"><path d="M56 1h24l-12 5z"/><path d="M125 1h24l-12 5z"/><path d="M193 1h24l-12 5z"/><path d="M262 1h24l-12 5z"/></g>
  </svg>
  <div class="abs center" style="left:34px;top:118px;width:67px"><div class="item-head" style="color:var(--white)">LOREM IPSUM</div><p class="item-text" style="color:var(--white)">Lorem ipsum dolor sit<br>amet, consectetuer</p></div>
  <div class="abs center" style="left:102px;top:118px;width:67px"><div class="item-head" style="color:var(--white)">LOREM IPSUM</div><p class="item-text" style="color:var(--white)">Lorem ipsum dolor sit<br>amet, consectetuer</p></div>
  <div class="abs center" style="left:171px;top:118px;width:67px"><div class="item-head" style="color:var(--white)">LOREM IPSUM</div><p class="item-text" style="color:var(--white)">Lorem ipsum dolor sit<br>amet, consectetuer</p></div>
  <div class="abs center" style="left:239px;top:118px;width:67px"><div class="item-head" style="color:var(--white)">LOREM IPSUM</div><p class="item-text" style="color:var(--white)">Lorem ipsum dolor sit<br>amet, consectetuer</p></div>
  <p class="abs body-copy" style="left:32px;top:144px;width:275px;text-align:justify;color:var(--beige)">Lorem ipsum dolor sit amet, consectetuer adipiscing elit, sed diam nonummy nibh euismod tincidunt ut laoreet dolore magna aliquam erat volutpat. Ut wisi enim ad minim veniam, quis nostrud exerci tation ullamcorper suscipit lobortis nisl ut aliquip ex ea commodo consequat. Duis autem vel eum iriure dolor in hendrerit in vulputate velit esse molestie consequat, vel illum dolore eu feugiat nulla</p>
  <div class="brand foot" style="color:var(--white)"><i class="brand-mark" style="background:var(--white)"></i>KALV</div>
  <div class="bar-bottom" style="height:1.5px;background:var(--white)"></div>
</section>

<!-- Slide 8: cross -->
<section class="slide" style="left:431px;top:455px">
  <h2 class="title">LOREM IPSUM</h2>
  <p class="subtitle">Lorem ipsum dolor sit amet, consectetuer</p>
  <div class="abs" style="left:19px;top:40px;width:57px;height:1.2px;background:var(--red)"></div>
  <svg class="abs" style="left:0;top:0" width="339" height="201">
    <path d="M149 61h33v34h35v34h-35v34h-33v-34h-36v-34h36z" fill="#c4121f"/>
    <path d="M165.5 120c-8-6-12-10-12-14a5 5 0 0 1 12-2 5 5 0 0 1 12 2c0 4-4 8-12 14z" fill="#fff"/>
    <polyline points="154,110 160,110 162,105 165,116 168,103 170,110 177,110" fill="none" stroke="#c4121f" stroke-width="1"/>
    <g fill="#e6e6e6" font-family="Montserrat,Arial,sans-serif" font-weight="700" font-size="15" text-anchor="middle">
      <text x="166" y="83">1</text><text x="201" y="118">2</text><text x="166" y="154">3</text><text x="131" y="118">4</text>
    </g>
  </svg>
  <div class="abs" style="left:191px;top:67px;width:80px"><div class="item-head">LOREM IPSUM</div><p class="item-text">Lorem ipsum dolor sit amet,<br>consectetuer adipiscing elit, sed<br>diam nonummy nibh</p></div>
  <div class="abs" style="left:227px;top:103px;width:80px"><div class="item-head">LOREM IPSUM</div><p class="item-text">Lorem ipsum dolor sit amet,<br>consectetuer adipiscing elit, sed<br>diam nonummy nibh</p></div>
  <div class="abs" style="left:25px;top:104px;width:80px;text-align:right"><div class="item-head">LOREM IPSUM</div><p class="item-text">Lorem ipsum dolor sit amet,<br>consectetuer adipiscing elit, sed<br>diam nonummy nibh</p></div>
  <div class="abs" style="left:60px;top:139px;width:80px;text-align:right"><div class="item-head">LOREM IPSUM</div><p class="item-text">Lorem ipsum dolor sit amet,<br>consectetuer adipiscing elit, sed<br>diam nonummy nibh</p></div>
  <div class="brand foot"><i class="brand-mark"></i>KALV</div>
  <div class="bar-bottom" style="background:var(--blue)"></div>
</section>

<!-- Slide 9: columns -->
<section class="slide" style="left:795px;top:455px;background:var(--white)">
  <div class="col" style="left:0">
    <div class="col-num">01</div>
    <svg class="abs" style="left:23px;top:41px;color:var(--blue)" width="22" height="28"><use href="#pin" width="22" height="28"/></svg>
    <svg class="abs" style="left:28px;top:46px;color:#fff" width="12" height="12"><use href="#ico-clipboard"/></svg>
    <div class="col-head">LOREM</div><div class="col-line" style="top:115px">DOLOR</div><div class="col-line" style="top:127px">SIT</div><div class="col-line" style="top:139px">AMET</div><div class="col-tag">dolor sit amet,</div>
  </div>
  <div class="col" style="left:68px">
    <div class="col-num">02</div>
    <svg class="abs" style="left:23px;top:41px;color:var(--blue)" width="22" height="28"><use href="#pin" width="22" height="28"/></svg>
    <svg class="abs" style="left:28px;top:46px;color:#fff" width="12" height="12"><use href="#ico-steth"/></svg>
    <div class="col-head">LOREM</div><div class="col-line" style="top:115px">DOLOR</div><div class="col-line" style="top:127px">SIT</div><div class="col-line" style="top:139px">AMET</div><div class="col-tag">dolor sit amet,</div>
  </div>
  <div class="col active" style="left:136px;top:1px;height:196px">
    <div class="col-num">03</div>
    <svg class="abs" style="left:19px;top:38px;color:#fff" width="30" height="38"><use href="#pin" width="30" height="38"/></svg>
    <svg class="abs" style="left:26px;top:45px;color:var(--red)" width="16" height="16"><use href="#ico-gauge"/></svg>
    <div class="col-head">LOREM</div><div class="col-line" style="top:115px">DOLOR</div><div class="col-line" style="top:127px">SIT</div><div class="col-line" style="top:139px">AMET</div><div class="col-tag">dolor sit amet,</div>
  </div>
  <div class="col" style="left:204px">
    <div class="col-num">04</div>
    <svg class="abs" style="left:23px;top:41px;color:var(--blue)" width="22" height="28"><use href="#pin" width="22" height="28"/></svg>
    <svg class="abs" style="left:28px;top:46px;color:#fff" width="12" height="12"><use href="#ico-kit"/></svg>
    <div class="col-head">LOREM</div><div class="col-line" style="top:115px">DOLOR</div><div class="col-line" style="top:127px">SIT</div><div class="col-line" style="top:139px">AMET</div><div class="col-tag">dolor sit amet,</div>
  </div>
  <div class="col" style="left:272px">
    <div class="col-num">05</div>
    <svg class="abs" style="left:23px;top:41px;color:var(--blue)" width="22" height="28"><use href="#pin" width="22" height="28"/></svg>
    <svg class="abs" style="left:28px;top:46px;color:#fff" width="12" height="12"><use href="#ico-chart"/></svg>
    <div class="col-head">LOREM</div><div class="col-line" style="top:115px">DOLOR</div><div class="col-line" style="top:127px">SIT</div><div class="col-line" style="top:139px">AMET</div><div class="col-tag">dolor sit amet,</div>
  </div>
  <div class="brand foot"><i class="brand-mark"></i>KALV</div>
  <div class="bar-bottom"></div>
</section>

</body>
</html>
```